Real Estate "For Sale" Sign for construction company

We need a sign that we can use to hang on a post and place on the road when we sell a property. The sign will be simple and will need to mainly feature our logo (files attached), as well as the words "For Sale", and then our phone number "(555) 617 3489". The sign will hang on a post that'll look something like the attached picture.

Target Market(s)

Home buyers

Industry/Entity Type

Real Estate

Font styles to use
Serif
Sans Serif

Colors
0054AA
0677BA
7BADD7
CADEEF
E8F1F8
0094D4
00A9DD
6FCCEA
C7EBF8
E9F6FB

Requirements
Must have
• For Sale & our phone number

```html
<!DOCTYPE html>
<html lang="en">
<head>
<meta charset="utf-8">
<title>For Sale Sign</title>
<link rel="stylesheet" href="https://fonts.googleapis.com/css2?family=Bebas+Neue&family=Questrial&display=swap">
<style>
  :root {
    --brand-blue: #1f88cc;
    --name-blue: #22a3dd;
    --navy: #1c2249;
    --white: #ffffff;
    --sky: #d7ecf8;
    --mist: #dde3ee;
    --page: #ffffff;
  }
  * { box-sizing: border-box; margin: 0; padding: 0; }
  html, body {
    width: 1200px; height: 828px; overflow: hidden;
    background: var(--page);
  }
  .canvas { position: relative; width: 1200px; height: 828px; }
  .sign {
    position: absolute; left: 321px; top: 14px;
    width: 558px; height: 800px;
    background: var(--white);
    box-shadow: 0 0 3px rgba(0,0,0,.35);
    overflow: hidden;
  }
  .brand {
    position: absolute; top: 34px; left: 0; width: 100%;
    text-align: center; color: var(--brand-blue);
    font-family: "Questrial", sans-serif;
  }
  .brand-mark {
    width: 96px; height: 96px; border-radius: 50%;
    background: var(--brand-blue); margin: 0 auto 14px;
  }
  .brand-name { font-size: 44px; line-height: 1; letter-spacing: .5px; }
  .brand-rule {
    position: absolute; top: 199px; left: 20px; right: 20px;
    height: 6px; background: var(--brand-blue);
  }
  .backdrop {
    position: absolute; top: 300px; left: 0; width: 100%; height: 261px;
    background: linear-gradient(180deg, rgba(215,236,248,0) 0%, var(--sky) 30%, var(--mist) 70%, #e9edf4 100%);
  }
  .agent {
    position: absolute; top: 214px; left: 0; width: 100%;
    text-align: center; color: var(--name-blue);
    font-family: "Questrial", sans-serif;
    font-size: 104px; line-height: 96px;
  }
  .contact {
    position: absolute; top: 414px; left: 0; width: 100%;
    text-align: center; color: var(--navy);
  }
  .contact-label { font-family: "Questrial", sans-serif; font-size: 25px; line-height: 1; }
  .contact-phone {
    font-family: "Bebas Neue", sans-serif; font-size: 94px; line-height: 84px;
    margin-top: 4px; letter-spacing: -1px;
  }
  .contact-web { font-family: "Questrial", sans-serif; font-size: 25px; line-height: 1; margin-top: 2px; }
  .status-band {
    position: absolute; left: 0; bottom: 0; width: 100%; height: 239px;
    background: var(--navy); color: var(--white);
    display: flex; align-items: center; justify-content: center;
    font-family: "Bebas Neue", sans-serif; font-size: 168px; letter-spacing: 5px;
    padding-top: 14px;
  }
</style>
</head>
<body>
<div class="canvas">
  <div class="sign">
    <div class="brand">
      <div class="brand-mark"></div>
      <div class="brand-name">Ridgecrest Properties</div>
    </div>
    <div class="brand-rule"></div>
    <div class="backdrop" role="img" aria-label="Soft layered mountain ridges in pale blue and grey"></div>
    <div class="agent">DANA<br>WHITFIELD</div>
    <div class="contact">
      <p class="contact-label">CALL OR TEXT ME AT:</p>
      <p class="contact-phone">(555) 617 3489</p>
      <p class="contact-web">RIDGECRESTHOMES.COM</p>
    </div>
    <div class="status-band">FOR SALE</div>
  </div>
</div>
</body>
</html>
```